Need a sleek, professional business card design for a Web Development business

I need a unique business card designed for a web development company. It is also the parent company for any ventures I do, such as my ClipWave channel, startup ideas I have, etc. I am the single member of "Bright Harbor Code LLC." I will attach my basic logo here, so you will see the current color scheme and have the asset available. Thank you!

Target Market(s)

Startups, SMB's, Professionals

Industry/Entity Type

Business

Font styles to use
Other font styles liked:
• Lovello for headings is what I use, but not necessary.

Colors

Designer to choose colors to be used in the design.

Requirements
Nice to have
• Sleek is the word. Professional, modern, dark.
Should not have
• Any work from someone else's design. Lacking originality.

```html
<!DOCTYPE html>
<html lang="en">
<head>
<meta charset="utf-8">
<title>Bright Harbor Code LLC – Business Card</title>
<link rel="stylesheet" href="https://fonts.googleapis.com/css2?family=Josefin+Sans:wght@300;700&display=swap">
<style>
  :root {
    --card-bg: #e6eeed;
    --brand-pink: #f5417f;
    --band-start: #f03d86;
    --band-end: #ec9552;
    --mark-tone: #f7677a;
    --band-text: #ffffff;
  }
  * { margin: 0; padding: 0; box-sizing: border-box; }
  html, body {
    width: 1200px;
    height: 720px;
    overflow: hidden;
    background: var(--card-bg);
  }
  .card {
    position: relative;
    width: 1200px;
    height: 720px;
    overflow: hidden;
    font-family: "Josefin Sans", sans-serif;
  }
  .card__pattern {
    position: absolute;
    inset: 0;
    background: var(--card-bg);
  }
  .brand {
    position: absolute;
    left: 300px;
    top: 200px;
    display: flex;
    align-items: center;
    gap: 80px;
  }
  .brand__square {
    width: 220px;
    height: 220px;
    background: var(--mark-tone);
    flex: none;
  }
  .brand__name {
    color: var(--brand-pink);
    font-weight: 700;
    font-size: 52px;
    line-height: 1.12;
    letter-spacing: 2px;
    text-transform: uppercase;
  }
  .url-band {
    position: absolute;
    left: 0;
    top: 574px;
    width: 1200px;
    height: 64px;
    background: linear-gradient(90deg, var(--band-start), var(--band-end));
    display: flex;
    align-items: center;
    justify-content: center;
  }
  .url-band__text {
    color: var(--band-text);
    font-weight: 300;
    font-size: 24px;
    letter-spacing: 2px;
    text-transform: uppercase;
    padding-top: 4px;
  }
</style>
</head>
<body>
  <div class="card">
    <div class="card__pattern" role="img" aria-label="Faint repeating scalloped wave pattern in pale grey-green"></div>

    <div class="brand">
      <div class="brand__square"></div>
      <h1 class="brand__name">Bright Harbor<br>Code</h1>
    </div>

    <div class="url-band">
      <p class="url-band__text">www.brightharborcode.com</p>
    </div>
  </div>
</body>
</html>
```